Brightmoor Partners Branding Revamp

We are a consulting company, looking for a way to display and promote our brand. We have 2 sides to the business- Brightmoor (financial) and Partners (cyber security). The financial side products relate to business necessities: card processing, website design/hosting/maintenance, VoIP phone systems. The cyber security side promotes a bundled package of 4 solutions: network vulnerability scan, dark web scan, anti-ransomeware/malware software, and image-level backups. We want people to understand that partnering with Brightmoor Partners gives them “Quiet Strength at Work” (tagline). Current badge and logos uploaded.

Target Market(s)

Small businesses

Contact Information for Business Card

Lena Marwick, Vice President, lena@brightmoorpartners.example, 555-806-1937, www.brightmoorpartners.example

Requirements
Nice to have
• I do prefer the darker background for front and back

```html
<!DOCTYPE html>
<html lang="en">
<head>
<meta charset="utf-8">
<title>Brightmoor Partners – Business Card</title>
<link rel="stylesheet" href="https://fonts.googleapis.com/css2?family=Questrial&family=Michroma&display=swap">
<style>
  :root {
    --page-bg: #1b1b1b;
    --card-bg: #2a2a2b;
    --card-sheen: #323233;
    --text-light: #e6e6e6;
    --text-muted: #bdbdbd;
    --accent-red: #d8343a;
    --accent-red-dim: #8e2226;
  }
  * { margin: 0; padding: 0; box-sizing: border-box; }
  html, body {
    width: 1200px; height: 675px; overflow: hidden;
    background: var(--page-bg);
    font-family: "Questrial", "Helvetica Neue", Arial, sans-serif;
    color: var(--text-light);
  }
  .canvas {
    position: relative; width: 1200px; height: 675px;
    display: flex; align-items: center; justify-content: center; gap: 40px;
  }
  .card {
    position: relative; width: 540px; height: 310px; overflow: hidden;
    background: linear-gradient(125deg, var(--card-sheen) 0%, var(--card-bg) 45%, var(--card-bg) 100%);
    box-shadow: 0 18px 40px rgba(0,0,0,.45);
  }

  /* Front */
  .brand-lockup { position: absolute; left: 34px; top: 30px; display: flex; align-items: center; gap: 12px; }
  .brand-lockup .mark-square { width: 12px; height: 12px; background: var(--accent-red); }
  .brand-lockup .brand-name { font-size: 13px; color: var(--accent-red); letter-spacing: .5px; }
  .brand-lockup .divider { width: 1px; height: 42px; background: var(--accent-red); margin-left: 4px; }
  .person-name { font-size: 21px; color: var(--text-light); }
  .person-title { font-size: 12px; color: var(--text-muted); margin-top: 4px; }

  .contact-list { position: absolute; left: 34px; top: 100px; list-style: none; font-size: 14px; }
  .contact-list li { display: flex; align-items: center; gap: 12px; margin-bottom: 10px; }
  .contact-list svg { width: 10px; height: 10px; fill: var(--text-muted); }

  .rule-front { position: absolute; left: 0; top: 160px; width: 285px; height: 1px; background: var(--accent-red); }
  .wordmark-front {
    position: absolute; left: 300px; top: 151px;
    font-family: "Michroma", "Questrial", sans-serif; font-size: 15px;
    letter-spacing: 6px; color: var(--text-light);
  }

  .offer-block { position: absolute; left: 72px; top: 176px; }
  .offer-title { font-size: 15px; margin-bottom: 10px; }
  .offer-list { list-style: none; font-size: 13.5px; line-height: 20px; }
  .offer-list li { display: flex; align-items: center; gap: 16px; }
  .offer-list svg { width: 10px; height: 10px; flex: none; }
  .offer-list circle { fill: none; stroke: var(--accent-red); stroke-width: 1.6; }

  .website { position: absolute; left: 150px; bottom: 18px; font-size: 13px; letter-spacing: 4px; color: var(--text-light); }

  /* Back */
  .tagline { position: absolute; left: 140px; top: 44px; font-size: 12px; letter-spacing: 4px; color: var(--text-light); }
  .corner-square { position: absolute; right: 40px; top: 38px; width: 18px; height: 18px; background: #6d6d6f; }
  .wordmark-back {
    position: absolute; left: 120px; top: 140px;
    font-family: "Michroma", "Questrial", sans-serif; font-size: 14px;
    letter-spacing: 5px; color: var(--accent-red);
  }
  .rule-back { position: absolute; left: 290px; top: 148px; right: 0; height: 1px; background: var(--accent-red-dim); }
  .solutions { position: absolute; right: 38px; top: 166px; text-align: right; color: var(--accent-red); }
  .solutions-title { font-size: 12.5px; margin-bottom: 6px; padding-right: 20px; }
  .solutions-list { list-style: none; font-size: 12.5px; line-height: 17px; }
  .solutions-list li { display: flex; justify-content: flex-end; align-items: center; gap: 10px; }
  .solutions-list svg { width: 9px; height: 9px; }
  .solutions-list circle { fill: none; stroke: var(--text-light); stroke-width: 1.6; }
</style>
</head>
<body>
<main class="canvas">

  <section class="card card-front" aria-label="Business card front">
    <div class="brand-lockup">
      <span class="mark-square"></span>
      <span class="brand-name">Brightmoor</span>
      <span class="divider"></span>
      <div>
        <div class="person-name">Lena Marwick</div>
        <div class="person-title">Vice President</div>
      </div>
    </div>

    <ul class="contact-list">
      <li>
        <svg viewBox="0 0 10 10" aria-hidden="true"><path d="M0 2h10v6H0z M0 2l5 3.5L10 2" /></svg>
        lena@brightmoorpartners.example
      </li>
      <li>
        <svg viewBox="0 0 10 10" aria-hidden="true"><path d="M2 0l2 2.5-1 1.2c.7 1.4 1.8 2.5 3.2 3.2l1.2-1L10 8 8.5 10C4 9.5.5 6 0 1.5z"/></svg>
        555-806-1937
      </li>
    </ul>

    <div class="rule-front"></div>
    <div class="wordmark-front">BRIGHTMOOR</div>

    <div class="offer-block">
      <div class="offer-title">Business Necessities</div>
      <ul class="offer-list">
        <li><svg viewBox="0 0 10 10" aria-hidden="true"><circle cx="5" cy="5" r="4"/></svg>Card processing</li>
        <li><svg viewBox="0 0 10 10" aria-hidden="true"><circle cx="5" cy="5" r="4"/></svg>website Design / Hosting / Maintenance</li>
        <li><svg viewBox="0 0 10 10" aria-hidden="true"><circle cx="5" cy="5" r="4"/></svg>VoIP phone systems</li>
      </ul>
    </div>

    <div class="website">www.brightmoorpartners.example</div>
  </section>

  <section class="card card-back" aria-label="Business card back">
    <div class="tagline">Quiet Strength at Work</div>
    <span class="corner-square"></span>

    <div class="wordmark-back">PARTNERS</div>
    <div class="rule-back"></div>

    <div class="solutions">
      <div class="solutions-title">4 Solutions</div>
      <ul class="solutions-list">
        <li>Network vulnerability scan <svg viewBox="0 0 10 10" aria-hidden="true"><circle cx="5" cy="5" r="4"/></svg></li>
        <li>Dark web scan <svg viewBox="0 0 10 10" aria-hidden="true"><circle cx="5" cy="5" r="4"/></svg></li>
        <li>Anti-Ransomware / Malware software <svg viewBox="0 0 10 10" aria-hidden="true"><circle cx="5" cy="5" r="4"/></svg></li>
        <li>Image level backups <svg viewBox="0 0 10 10" aria-hidden="true"><circle cx="5" cy="5" r="4"/></svg></li>
      </ul>
    </div>
  </section>

</main>
</body>
</html>
```